Website for dental practice Fully customized wordpress theme

Dentist website
Simple and uncluttered
Updates

Please see updated messages and uploaded file to see what I would like to have included in final design

Target Market(s)

Dental Patients

Industry/Entity Type

Dental

Font styles to use
Serif

Colors
0455a3
85abd2
3276b4
ffffff

Requirements
Must have
• Must have two big red blinking buttons that says "Leave a zindle review" and "Leave a Pelmora Review"
• Simple and uncluttered
• Big prominent phone number
• Have logo as part of a blue stripe across the top of the website as a header
• Curves and swirls and part of design
• Multilingual support for english and Hebrew websites
• Fully customized wordpress theme
• SEO optimization
• 3. Multi-lingual support hebrew and english button
• 6. Inclusion of Zindle Charts Hagefen 4 Rehovot
• Please incorporate the logo with the blue stripe across the website as seen in the business card attached. Please see sketch
Nice to have
• Please crop and edit photographs for best appearance
• I like curves and swirls
• Sliders are nice

```html
<!DOCTYPE html>
<html lang="en">
<head>
<meta charset="utf-8">
<title>Lior Dental</title>
<link href="https://fonts.googleapis.com/css2?family=Open+Sans:wght@400;600;700&display=swap" rel="stylesheet">
<style>
  :root {
    --brand-blue: #1f6fb8;
    --deep-blue: #0455a3;
    --stripe-blue: #0a63cc;
    --soft-blue: #85abd2;
    --review-red: #c00000;
    --star-yellow: #ffe600;
    --ink: #111111;
    --white: #ffffff;
    --hero-a: #dfeef0;
    --hero-b: #b9d7dc;
  }
  * { box-sizing: border-box; margin: 0; padding: 0; }
  html, body { width: 1200px; height: 593px; overflow: hidden; background: var(--white); }
  body { font-family: "Open Sans", Arial, sans-serif; color: var(--ink); position: relative; }

  .site-header { position: absolute; left: 0; top: 0; width: 1200px; height: 87px; background: var(--white); }
  .contact-bar { position: absolute; top: 8px; left: 324px; display: flex; gap: 3px; }
  .contact-chip {
    height: 62px; background: var(--review-red); border-radius: 6px;
    box-shadow: 0 0 6px rgba(200,0,0,.55);
    display: flex; align-items: center; justify-content: center; gap: 10px;
    color: var(--white); font-weight: 700;
  }
  .chip-phone { width: 212px; font-size: 20px; }
  .chip-hours { width: 212px; font-size: 16px; }
  .chip-review { width: 159px; flex-direction: column; gap: 2px; }
  .review-stars { display: block; }
  .review-frame {
    width: 110px; height: 34px; border: 1px solid var(--white); border-radius: 3px;
    display: flex; flex-direction: column; align-items: center; justify-content: center;
  }
  .review-lead { font-size: 8px; font-weight: 600; line-height: 11px; }
  .review-name { font-size: 13px; font-weight: 600; line-height: 16px; letter-spacing: .5px; }

  .main-nav { position: absolute; left: 0; top: 87px; width: 1200px; height: 53px; background: var(--brand-blue); }
  .nav-home { position: absolute; left: 499px; top: 14px; color: var(--white); font-size: 13px; font-weight: 600; }
  .nav-flag { position: absolute; top: 20px; }
  .flag-en { left: 575px; }
  .flag-he { left: 630px; }
  .nav-search { position: absolute; left: 672px; top: 18px; }

  .brand-badge {
    position: absolute; left: 109px; top: 3px; width: 130px; height: 130px; border-radius: 50%;
    background: var(--white); display: flex; align-items: center; justify-content: center; z-index: 3;
  }
  .brand-name { color: var(--ink); font-size: 14px; font-weight: 600; margin-top: 40px; }

  .hero { position: absolute; left: 0; top: 140px; width: 1200px; height: 453px;
    background: linear-gradient(90deg, var(--hero-a) 0%, #cfe6ea 45%, var(--hero-b) 100%); overflow: hidden; }
  .hero-portrait { position: absolute; left: 0; top: 0; width: 470px; height: 453px;
    background: linear-gradient(90deg, #c2a08a 0%, #bf9d88 70%, rgba(207,230,234,0) 100%); }
  .hero-copy { position: absolute; left: 528px; top: 82px; width: 384px; }
  .hero-title { font-size: 41px; font-weight: 600; line-height: 1.2; text-shadow: 2px 2px 3px rgba(0,0,0,.3); }
  .hero-text { margin-top: 22px; font-size: 15.5px; line-height: 30.6px; text-align: justify; text-shadow: 0 1px 2px rgba(255,255,255,.6); }
  .hero-button { display: inline-block; margin-top: 18px; width: 226px; height: 45px; border: 2px solid var(--ink);
    font-size: 18px; line-height: 41px; text-align: center; color: var(--ink); text-decoration: none; }
  .hero-swoosh { position: absolute; left: 0; top: 0; }
</style>
</head>
<body>
  <header class="site-header">
    <div class="contact-bar">
      <div class="contact-chip chip-phone">
        <svg width="30" height="30" viewBox="0 0 30 30" aria-hidden="true"><circle cx="15" cy="15" r="13.5" fill="none" stroke="#fff" stroke-width="2"/><path d="M10 8c1-1 2 0 3 2s0 2-1 3c1 2 3 4 5 5 1-1 1-2 3-1s3 2 2 3c-1 2-3 2-5 1-4-2-7-5-8-9 0-2 0-3 1-4z" fill="#fff"/></svg>
        <span>+198765432</span>
      </div>
      <div class="contact-chip chip-hours">
        <svg width="32" height="32" viewBox="0 0 32 32" aria-hidden="true"><circle cx="16" cy="16" r="14.5" fill="none" stroke="#fff" stroke-width="2"/><path d="M16 7v9l7 4" fill="none" stroke="#fff" stroke-width="2"/></svg>
        <span>9:00AM -5:00PM</span>
      </div>
      <div class="contact-chip chip-review">
        <svg class="review-stars" width="92" height="16" viewBox="0 0 92 16" aria-hidden="true"><g fill="var(--star-yellow)"><polygon points="8,0 10,6 16,6 11,10 13,16 8,12 3,16 5,10 0,6 6,6"/><polygon transform="translate(19 0)" points="8,0 10,6 16,6 11,10 13,16 8,12 3,16 5,10 0,6 6,6"/><polygon transform="translate(38 0)" points="8,0 10,6 16,6 11,10 13,16 8,12 3,16 5,10 0,6 6,6"/><polygon transform="translate(57 0)" points="8,0 10,6 16,6 11,10 13,16 8,12 3,16 5,10 0,6 6,6"/><polygon transform="translate(76 0)" points="8,0 10,6 16,6 11,10 13,16 8,12 3,16 5,10 0,6 6,6"/></g></svg>
        <div class="review-frame"><span class="review-lead">Please review us on</span><span class="review-name">zindle</span></div>
      </div>
      <div class="contact-chip chip-review">
        <svg class="review-stars" width="92" height="16" viewBox="0 0 92 16" aria-hidden="true"><g fill="var(--star-yellow)"><polygon points="8,0 10,6 16,6 11,10 13,16 8,12 3,16 5,10 0,6 6,6"/><polygon transform="translate(19 0)" points="8,0 10,6 16,6 11,10 13,16 8,12 3,16 5,10 0,6 6,6"/><polygon transform="translate(38 0)" points="8,0 10,6 16,6 11,10 13,16 8,12 3,16 5,10 0,6 6,6"/><polygon transform="translate(57 0)" points="8,0 10,6 16,6 11,10 13,16 8,12 3,16 5,10 0,6 6,6"/><polygon transform="translate(76 0)" points="8,0 10,6 16,6 11,10 13,16 8,12 3,16 5,10 0,6 6,6"/></g></svg>
        <div class="review-frame"><span class="review-lead">Please review us on</span><span class="review-name">Pelmora</span></div>
      </div>
    </div>
  </header>

  <nav class="main-nav">
    <span class="nav-home">Home</span>
    <svg class="nav-flag flag-en" width="18" height="11" viewBox="0 0 18 11" aria-label="English"><rect width="18" height="11" fill="#1d3f8f"/><path d="M0 0L18 11M18 0L0 11" stroke="#fff" stroke-width="2"/><path d="M9 0v11M0 5.5h18" stroke="#fff" stroke-width="3.5"/><path d="M9 0v11M0 5.5h18" stroke="#c8102e" stroke-width="2"/></svg>
    <svg class="nav-flag flag-he" width="18" height="11" viewBox="0 0 18 11" aria-label="Hebrew"><rect width="18" height="11" fill="#fff"/><rect y="1.5" width="18" height="1.5" fill="#1d3f8f"/><rect y="8" width="18" height="1.5" fill="#1d3f8f"/><polygon points="9,3.5 11,7 7,7" fill="none" stroke="#1d3f8f" stroke-width=".6"/></svg>
    <svg class="nav-search" width="18" height="18" viewBox="0 0 18 18" aria-label="Search"><circle cx="10" cy="7" r="5.5" fill="none" stroke="#444" stroke-width="1.4"/><path d="M6 11l-5 5" stroke="#444" stroke-width="1.6"/></svg>
  </nav>

  <div class="brand-badge"><span class="brand-name">Lior Dental</span></div>

  <section class="hero">
    <div class="hero-portrait" role="img" aria-label="Portrait photograph of the dentist"></div>
    <div class="hero-copy">
      <h1 class="hero-title">Lior Dental</h1>
      <p class="hero-text">orem ipsum dolor sit amet, consectetur adipiscing elit. Praesent sed lacinia ex, eget auctor nisi. Maecenas sed dictum nulla, eu malesuada nisl. Pellentesque faucibus dolor ac euismod venenatis.</p>
      <a class="hero-button" href="#">Make an Appointment</a>
    </div>
    <svg class="hero-swoosh" width="1200" height="453" viewBox="0 0 1200 453" aria-hidden="true">
      <path d="M420 453 C700 400 950 345 1200 332 L1200 453 Z" fill="var(--white)"/>
      <path d="M520 453 C760 410 980 365 1200 350 L1200 362 C990 378 780 418 600 453 Z" fill="var(--stripe-blue)"/>
    </svg>
  </section>
</body>
</html>
```